VELU Medical Spa

We'd like a business card with the reverse of the card for appointments. We like round corners and vertical design. We have a background image and bird logo to include with the following wording on the front:-
Velu Medical Spa
248 Pembury Street
NORTH ADELAIDE
SA 5006
Phone 08 83915746
www.velumedicalspa.com.au
Facebook velumedicalspa
Instagram velumedicalspa
On the back I'd like an appointment card layout please.
Cheers Dee

```html
<!DOCTYPE html>
<html lang="en">
<head>
<meta charset="utf-8">
<title>Velu Medical Spa – Business &amp; Appointment Card</title>
<link rel="stylesheet" href="https://fonts.googleapis.com/css2?family=Cinzel:wght@400&family=Cormorant+Garamond:wght@400&family=Lato:ital,wght@0,400;1,400&family=Arimo:wght@400;700&display=swap">
<style>
  :root {
    --page-bg: #e6e6e6;
    --mint-light: #dcf3e8;
    --mint-soft: #c3eadb;
    --mint: #abdcc0;
    --mint-deep: #86d2b9;
    --strip: #161616;
    --ink: #4f5553;
    --rule: #8fa39c;
    --white: #ffffff;
  }
  * { box-sizing: border-box; margin: 0; padding: 0; }
  html, body { width: 1200px; height: 1200px; overflow: hidden; }
  body { background: var(--page-bg); position: relative; }

  .card {
    position: absolute;
    top: 304px;
    width: 360px;
    height: 592px;
    border-radius: 18px;
    overflow: hidden;
  }

  /* Appointment side */
  .appointment-card {
    left: 203px;
    background: linear-gradient(180deg, var(--mint-light) 0%, var(--mint-soft) 100%);
  }
  .foliage {
    position: absolute;
    right: 0; bottom: 0;
    width: 100%; height: 70%;
    background: radial-gradient(ellipse at 80% 85%, rgba(140, 205, 200, 0.45) 0%, rgba(140, 205, 200, 0) 70%);
  }
  .appointment-title {
    position: absolute;
    top: 108px; left: 0; width: 100%;
    text-align: center;
    font-family: "Cinzel", serif;
    font-weight: 400;
    font-size: 32px;
    line-height: 37px;
    color: var(--white);
  }
  .field {
    position: absolute;
    left: 52px;
    width: 259px;
    border-bottom: 1px solid var(--rule);
    font-family: "Lato", sans-serif;
    font-size: 21px;
    color: var(--ink);
    padding-bottom: 4px;
  }
  .field-name { top: 246px; }
  .field-date { top: 313px; }
  .field-time { top: 380px; }
  .notice {
    position: absolute;
    bottom: 28px; left: 0; width: 100%;
    text-align: center;
    font-family: "Lato", sans-serif;
    font-style: italic;
    font-size: 16.5px;
    line-height: 22px;
    color: var(--ink);
  }

  /* Contact side */
  .contact-card {
    left: 602px;
    background: linear-gradient(180deg, var(--mint) 0%, var(--mint) 45%, var(--mint-deep) 100%);
  }
  .contact-card .foliage {
    background: radial-gradient(ellipse at 85% 80%, rgba(120, 200, 190, 0.55) 0%, rgba(120, 200, 190, 0) 70%);
  }
  .side-strip {
    position: absolute;
    left: 0; top: 0;
    width: 40px; height: 100%;
    background: var(--strip);
  }
  .brand-name {
    position: absolute;
    top: 190px; left: 40px; right: 0;
    text-align: center;
    font-family: "Cormorant Garamond", serif;
    font-size: 50px;
    letter-spacing: 16px;
    padding-left: 16px;
    color: var(--white);
  }
  .rule {
    position: absolute;
    height: 1px;
    background: var(--white);
  }
  .rule-brand { top: 293px; left: 143px; width: 78px; }
  .rule-a { top: 413px; left: 53px; width: 95px; }
  .rule-b { top: 490px; left: 53px; width: 95px; }

  .icon {
    position: absolute;
    left: 8px;
    width: 22px; height: 22px;
  }
  .contact-text {
    position: absolute;
    left: 50px;
    font-family: "Arimo", sans-serif;
    color: var(--white);
    font-size: 16.5px;
    line-height: 21px;
  }
  .spa-name { font-weight: 700; font-size: 19px; line-height: 22px; }
  .address { top: 334px; }
  .phone-web { top: 429px; }
  .socials { top: 508px; left: 52px; line-height: 27px; }
</style>
</head>
<body>

<section class="card appointment-card">
  <div class="foliage" role="img" aria-label="Soft palm leaf background"></div>
  <h1 class="appointment-title">YOUR NEXT<br>APPOINTMENT</h1>
  <div class="field field-name">NAME :</div>
  <div class="field field-date">DATE :</div>
  <div class="field field-time">TIME :</div>
  <p class="notice">If unable to keep appointment<br>kindly give 24hrs notice</p>
</section>

<section class="card contact-card">
  <div class="foliage" role="img" aria-label="Soft palm leaf background"></div>
  <div class="side-strip"></div>

  <div class="brand-name">VELU</div>
  <div class="rule rule-brand"></div>

  <svg class="icon" style="top:335px" viewBox="0 0 22 22" aria-hidden="true">
    <circle cx="11" cy="11" r="9.5" fill="none" stroke="var(--mint)" stroke-width="1.8"/>
    <path d="M11 16 C8 12.5 7.5 11 7.5 9.5 a3.5 3.5 0 0 1 7 0 c0 1.5 -0.5 3 -3.5 6.5z" fill="none" stroke="var(--mint)" stroke-width="1.5"/>
    <circle cx="11" cy="9.5" r="1.2" fill="var(--mint)"/>
  </svg>
  <div class="contact-text address">
    <div class="spa-name">VELU MEDICAL SPA</div>
    248 Pembury Street<br>WEST HARTLAND, NV 7142
  </div>
  <div class="rule rule-a"></div>

  <svg class="icon" style="top:430px" viewBox="0 0 22 22" aria-hidden="true">
    <circle cx="11" cy="11" r="9.5" fill="none" stroke="var(--mint)" stroke-width="1.8"/>
    <path d="M7.5 6.5 l2 -0.5 1 2.5 -1.2 1 a6 6 0 0 0 3 3 l1 -1.2 2.5 1 -0.5 2 c-4 0.5 -8.5 -4 -7.8 -7.8z" fill="var(--mint)"/>
  </svg>
  <svg class="icon" style="top:452px" viewBox="0 0 22 22" aria-hidden="true">
    <circle cx="11" cy="11" r="9.5" fill="none" stroke="var(--mint)" stroke-width="1.8"/>
    <circle cx="11" cy="11" r="5" fill="none" stroke="var(--mint)" stroke-width="1.3"/>
    <path d="M6 11 h10 M11 6 c-2.5 3 -2.5 7 0 10 M11 6 c2.5 3 2.5 7 0 10" fill="none" stroke="var(--mint)" stroke-width="1"/>
  </svg>
  <div class="contact-text phone-web">
    08 83915746<br>www.velumedicalspa.com.au
  </div>
  <div class="rule rule-b"></div>

  <svg class="icon" style="top:510px" viewBox="0 0 22 22" aria-hidden="true">
    <rect x="2" y="2" width="18" height="18" rx="3" fill="var(--mint)"/>
  </svg>
  <svg class="icon" style="top:537px" viewBox="0 0 22 22" aria-hidden="true">
    <circle cx="11" cy="11" r="9" fill="none" stroke="var(--mint)" stroke-width="1.8"/>
  </svg>
  <div class="contact-text socials">
    velumedicalspa<br>velumedicalspa
  </div>
</section>

</body>
</html>
```